Figma App design and working prototype

I need to create a User Interface design and a Working prototype using Figma or similar. I’d also like all the assets and guidelines needed to guide the App developers to create the final product.
So, I'll need Design files and assets but you that I can give to an App development company or a freelance developer to create Android and iOS apps.

This app is an app for adults who wan to meet and have sex no strings attached.

The App name will be Velmora

I have attached an app some pictures and a pdf file explaining details of the apps functions.

This app will be a sexy version of the tavoru app with a personals section used for adult services. I have attached images and a pdf below that will tell you the functions of the app.

I need an app interface design done for an app idea I have. I am nee to this it is my first time trying to launch an app and I do not know what you need in order to get what I need. I need a site map/ design and if possible a working prototype that I can pass on to an app developer that can deliver the final product. This model will be used to raise funds and give investors an idea of what the apps functions will do as detailed in the project brief. Any advise would be greatly appreciated. Please let me know if you have any questions. Looking forward to working with you.

Target Market(s)

Adults men and women looking for some adult entertainment

Industry/Entity Type

Adult entertainment Strip clubs

Colors
E54698
E96AAD
F1A4CE
F9D9EA
FCEFF6
A7469A
B969AE
D3A5CF
EDDBEB
F8F0F9
6B429C
8869AF
B7A5CE
E3DAEB
F3F0F8

Requirements
Must have
• An 18+ confirmation,
Nice to have
• A sexy feel.

```html
<!DOCTYPE html>
<html lang="en">
<head>
<meta charset="utf-8">
<title>Velmora — App screens</title>
<link href="https://fonts.googleapis.com/css2?family=Nunito:wght@400;600;700;800&display=swap" rel="stylesheet">
<style>
  :root{
    --canvas:#f3f4f7;
    --violet:#7a2be6;
    --violet-deep:#6a1fd6;
    --violet-soft:#9d63f2;
    --button:#a77cf3;
    --button-icon:#c4a4f8;
    --white:#ffffff;
    --ink:#23212a;
    --ink-soft:#6d6a78;
    --sheet:#f6f5f8;
    --badge-new:#e8463c;
    --chat-green:#3cc84a;
    --shadow:0 18px 40px rgba(80,40,140,.18);
  }
  *{box-sizing:border-box;margin:0;padding:0}
  html,body{width:946px;height:1200px;overflow:hidden;background:var(--canvas);
    font-family:"Nunito",Arial,sans-serif;color:var(--ink)}
  .board{position:relative;width:946px;height:1200px}

  .screen{position:absolute;top:60px;width:280px;height:606px;border-radius:36px;overflow:hidden;box-shadow:var(--shadow)}
  .screen--welcome{left:31px;background:linear-gradient(160deg,var(--violet-soft) 0%,var(--violet) 45%,var(--violet-deep) 100%)}
  .screen--browse{left:333px;background:linear-gradient(170deg,var(--violet-soft) 0%,var(--violet) 60%)}
  .screen--profile{left:635px;background:var(--sheet)}

  /* Welcome */
  .welcome__brand{position:absolute;top:58px;width:100%;text-align:center;color:var(--white);font-weight:600;font-size:40px;letter-spacing:.5px}
  .welcome__art{position:absolute;top:132px;left:60px;width:160px;height:110px;border-radius:50% 50% 46% 46%;
    background:radial-gradient(ellipse at 50% 45%,#e9dcff 0%,#b48af5 35%,#7d3ae8 75%)}
  .welcome__title{position:absolute;top:278px;width:100%;text-align:center;color:var(--white);font-weight:800;font-size:19px}
  .welcome__sub{position:absolute;top:304px;width:100%;text-align:center;color:#e6d8ff;font-size:12px}
  .gender-list{position:absolute;top:340px;left:44px;width:192px;display:flex;flex-direction:column;gap:14px}
  .gender{display:flex;align-items:center;height:44px;border-radius:12px;background:var(--button);color:var(--white);font-weight:700;font-size:13px}
  .gender__icon{width:44px;height:44px;border-radius:12px;background:var(--button-icon);display:flex;align-items:center;justify-content:center;margin-right:34px;box-shadow:0 6px 12px rgba(60,20,130,.25)}
  .welcome__legal{position:absolute;bottom:30px;left:26px;right:26px;text-align:center;color:#b99cf0;font-size:9.5px;line-height:1.5}
  .welcome__legal b{color:#e8dcff;font-weight:600}

  /* Browse */
  .search{position:absolute;top:46px;left:18px;right:66px;height:38px;border-radius:10px;background:var(--button);color:#ede2ff;font-size:11px;display:flex;align-items:center;padding:0 14px}
  .filter{position:absolute;top:46px;right:18px;width:38px;height:38px;border-radius:10px;background:var(--button);display:flex;align-items:center;justify-content:center}
  .grid{position:absolute;top:104px;left:18px;right:18px;display:grid;grid-template-columns:1fr 1fr;gap:12px}
  .card{background:var(--white);border-radius:14px;overflow:hidden;position:relative}
  .card--offset{margin-top:40px}
  .card__photo{height:150px}
  .card__name{height:28px;display:flex;align-items:center;justify-content:center;font-size:11px;font-weight:700}
  .card__tick{position:absolute;top:8px;right:8px;width:16px;height:16px;border-radius:50%;background:var(--button-icon);display:flex;align-items:center;justify-content:center}
  .card__new{position:absolute;top:128px;left:0;background:var(--badge-new);color:var(--white);font-size:8px;font-weight:800;padding:2px 8px;border-radius:0 8px 8px 0}
  .card--faded{opacity:.35}
  .photo-rose{background:linear-gradient(160deg,#c97a86,#6b4a4f)}
  .photo-gold{background:linear-gradient(160deg,#f2c14e,#c98f3a)}
  .photo-pink{background:linear-gradient(160deg,#f6a8b3,#d9707f)}
  .photo-sand{background:linear-gradient(160deg,#d8cbb8,#8c7a66)}
  .photo-violet{background:linear-gradient(160deg,#a77cf3,#7a2be6)}

  /* Profile */
  .profile__photo{position:absolute;top:0;left:0;right:0;height:310px;background:linear-gradient(170deg,#f3efe9 0%,#d9a78e 50%,#8b7a70 100%)}
  .back{position:absolute;top:40px;left:18px;width:32px;height:32px;border-radius:9px;background:var(--button-icon);display:flex;align-items:center;justify-content:center}
  .sheet{position:absolute;top:270px;left:0;right:0;bottom:0;background:var(--white);border-radius:26px 26px 0 0;padding:18px 18px 0}
  .sheet__head{display:flex;align-items:center;gap:10px}
  .avatar{width:38px;height:38px;border-radius:50%;background:linear-gradient(160deg,#d9a78e,#7b5a4c)}
  .sheet__name{font-weight:800;font-size:13px}
  .sheet__seen{font-size:9.5px;color:var(--ink-soft)}
  .contacts{margin-left:auto;display:flex;gap:6px}
  .contact{width:24px;height:24px;border-radius:50%;display:flex;align-items:center;justify-content:center}
  .contact--chat{background:var(--chat-green)}
  .contact--call{background:var(--violet-soft)}
  .sheet__bio{margin-top:12px;font-size:9.5px;line-height:1.55;color:var(--ink-soft)}
  .facts{position:absolute;left:0;right:0;bottom:0;height:150px;padding:40px 18px 0;
    background:linear-gradient(180deg,rgba(255,255,255,0) 0%,#d6c2fb 40%,var(--violet-soft) 100%)}
  .fact{display:grid;grid-template-columns:70px 1fr;font-size:10px;line-height:1.8}
  .fact dt{font-weight:800}
  .fact dd{color:#4a3a6e}

  .wordmark{position:absolute;top:850px;left:0;right:0;text-align:center;color:var(--violet);font-weight:600;font-size:130px;letter-spacing:1px}
</style>
</head>
<body>
<main class="board">

  <section class="screen screen--welcome" aria-label="Gender selection">
    <div class="welcome__brand">Velmora</div>
    <div class="welcome__art" role="img" aria-label="Glossy violet lips illustration"></div>
    <h1 class="welcome__title">Who are you?</h1>
    <p class="welcome__sub">Select your gender</p>
    <div class="gender-list">
      <div class="gender"><span class="gender__icon"><svg width="20" height="20" viewBox="0 0 20 20" fill="none" stroke="#fff" stroke-width="2"><circle cx="8" cy="12" r="5"/><path d="M12 8l5-5M12 3h5v5"/></svg></span>I am a Man</div>
      <div class="gender"><span class="gender__icon"><svg width="20" height="20" viewBox="0 0 20 20" fill="none" stroke="#fff" stroke-width="2"><circle cx="10" cy="7" r="5"/><path d="M10 12v7M7 16h6"/></svg></span>I am a Woman</div>
      <div class="gender"><span class="gender__icon"><svg width="20" height="20" viewBox="0 0 20 20" fill="none" stroke="#fff" stroke-width="2"><circle cx="10" cy="10" r="4"/><path d="M10 14v5M7.5 17h5M13 7l4-4M14 3h3v3M7 7L3 3M3 6V3h3"/></svg></span>I am a Trans</div>
    </div>
    <p class="welcome__legal">By continuing you confirm you are <b>18+</b>, have read this <b>agreement</b>, understood it and agree to be bound by it.</p>
  </section>

  <section class="screen screen--browse" aria-label="Browse profiles">
    <div class="search">Search names, location or city</div>
    <div class="filter"><svg width="16" height="16" viewBox="0 0 16 16" fill="none" stroke="#fff" stroke-width="1.8"><path d="M4 2v12M12 2v12"/><circle cx="4" cy="10" r="2" fill="#a77cf3"/><circle cx="12" cy="6" r="2" fill="#a77cf3"/></svg></div>
    <div class="grid">
      <article class="card">
        <div class="card__photo photo-rose" role="img" aria-label="Profile photo of Maren"></div>
        <span class="card__tick"><svg width="9" height="9" viewBox="0 0 10 10" fill="none" stroke="#fff" stroke-width="2"><path d="M2 5l2 2 4-4"/></svg></span>
        <div class="card__name">Maren</div>
      </article>
      <article class="card card--offset">
        <div class="card__photo photo-gold" role="img" aria-label="Profile photo of Solvi"></div>
        <span class="card__tick"><svg width="9" height="9" viewBox="0 0 10 10" fill="none" stroke="#fff" stroke-width="2"><path d="M2 5l2 2 4-4"/></svg></span>
        <div class="card__name">Solvi</div>
      </article>
      <article class="card">
        <div class="card__photo photo-pink" role="img" aria-label="Profile photo of Odessa"></div>
        <span class="card__tick"><svg width="9" height="9" viewBox="0 0 10 10" fill="none" stroke="#fff" stroke-width="2"><path d="M2 5l2 2 4-4"/></svg></span>
        <span class="card__new">NEW</span>
        <div class="card__name">Odessa</div>
      </article>
      <article class="card card--offset">
        <div class="card__photo photo-sand" role="img" aria-label="Profile photo of Liora"></div>
        <div class="card__name">Liora</div>
      </article>
      <article class="card card--faded">
        <div class="card__photo photo-violet" role="img" aria-label="Profile photo"></div>
      </article>
    </div>
  </section>

  <section class="screen screen--profile" aria-label="Profile detail">
    <div class="profile__photo" role="img" aria-label="Beach portrait photo of the profile owner"></div>
    <div class="back"><svg width="16" height="16" viewBox="0 0 16 16" fill="none" stroke="#7a2be6" stroke-width="1.8"><circle cx="8" cy="8" r="6.5"/><path d="M9 5L6 8l3 3M6 8h5"/></svg></div>
    <div class="sheet">
      <div class="sheet__head">
        <div class="avatar" role="img" aria-label="Avatar"></div>
        <div>
          <div class="sheet__name">Tamsin Vale</div>
          <div class="sheet__seen">Last seen online: 29.5.2022</div>
        </div>
        <div class="contacts">
          <span class="contact contact--chat"><svg width="12" height="12" viewBox="0 0 12 12" fill="#fff"><path d="M3 1l2 2-1 1.5c.6 1.3 1.6 2.3 3 3L8.5 6.5l2 2-1 2C5.5 10.5 1.5 6.5 1 2.5z"/></svg></span>
          <span class="contact contact--call"><svg width="12" height="12" viewBox="0 0 12 12" fill="#fff"><path d="M3 1l2 2-1 1.5c.6 1.3 1.6 2.3 3 3L8.5 6.5l2 2-1 2C5.5 10.5 1.5 6.5 1 2.5z"/></svg></span>
        </div>
      </div>
      <p class="sheet__bio">Hi boys. My name is NELL ........Just came here new . 19 years old. You will have the ability to enjoy. I can do what you like. I enjoy what I do. And I am sure you will too. All pictures 100% real. Provide incall services, overnight service ..........^_^please send message in my Chatsy only ..</p>
    </div>
    <dl class="facts">
      <div class="fact"><dt>Gender:</dt><dd>Female</dd></div>
      <div class="fact"><dt>Age:</dt><dd>19</dd></div>
      <div class="fact"><dt>Location:</dt><dd>Marisol City / Marisol</dd></div>
      <div class="fact"><dt>Eyes:</dt><dd>Black</dd></div>
    </dl>
  </section>

  <div class="wordmark">Velmora</div>
</main>
</body>
</html>
```